Business card for STEADYWAVE

Please design professional business card for IT consulting firm STEADYWAVE INC.
Use logo attached.
Use information from sample qNode business card attached.
replace qnode inc with STEADYWAVE INC.
as well as qnodeinc.com with steadywave.example

```html
<!DOCTYPE html>
<html lang="en">
<head>
<meta charset="utf-8">
<title>STEADYWAVE Business Card</title>
<link rel="stylesheet" href="https://fonts.googleapis.com/css2?family=PT+Sans:wght@400;700&display=swap">
<style>
  :root {
    --backdrop: #4f4f4f;
    --card: #f6f6f6;
    --ink: #111111;
    --text: #1e1e1e;
    --accent: #9b17d6;
    --faint-a: rgba(155, 23, 214, 0.06);
    --faint-b: rgba(40, 200, 220, 0.06);
  }
  * { margin: 0; padding: 0; box-sizing: border-box; }
  html, body {
    width: 1200px;
    height: 1200px;
    overflow: hidden;
    background: var(--backdrop);
    font-family: "PT Sans", Arial, sans-serif;
  }
  .card {
    position: absolute;
    left: 241px;
    width: 727px;
    height: 436px;
    background: var(--card);
  }
  .card--front { top: 114px; }
  .card--back { top: 635px; }

  .wordmark {
    position: absolute;
    display: flex;
    align-items: center;
    font-weight: 700;
    color: var(--ink);
    letter-spacing: 0.1em;
    white-space: nowrap;
  }
  .wordmark__square {
    display: inline-block;
    background: var(--accent);
  }
  .card--front .wordmark {
    left: 0;
    right: 0;
    top: 178px;
    justify-content: center;
    font-size: 60px;
    line-height: 1;
  }
  .card--front .wordmark__square {
    width: 28px; height: 28px; margin-left: 14px;
  }
  .card--back .wordmark {
    left: 47px;
    top: 70px;
    font-size: 40px;
    line-height: 1;
  }
  .card--back .wordmark__square {
    width: 19px; height: 19px; margin-left: 10px;
  }

  .decor-square {
    position: absolute;
    left: 440px;
    top: 35px;
    width: 215px;
    height: 215px;
    background: linear-gradient(135deg, var(--faint-b), var(--faint-a));
  }

  .person {
    position: absolute;
    left: 47px;
    top: 201px;
    color: var(--text);
    font-size: 15.5px;
    line-height: 20px;
  }
  .person__name {
    color: var(--accent);
    font-weight: 700;
    font-size: 27px;
    line-height: 28px;
    margin-bottom: 1px;
  }
  .person__credential { font-size: 14px; }

  .contact {
    position: absolute;
    left: 47px;
    top: 286px;
    color: var(--text);
    font-size: 16px;
    line-height: 22.5px;
  }
  .contact__label {
    color: var(--accent);
    margin-right: 8px;
  }

  .company {
    position: absolute;
    left: 416px;
    top: 311px;
    color: var(--text);
    font-size: 16px;
    line-height: 20.5px;
  }
  .company__name {
    color: var(--accent);
    font-weight: 700;
  }
</style>
</head>
<body>
  <section class="card card--front">
    <div class="wordmark">STEADYWAVE<span class="wordmark__square"></span></div>
  </section>

  <section class="card card--back">
    <div class="wordmark">STEADYWAVE<span class="wordmark__square"></span></div>
    <div class="decor-square"></div>

    <div class="person">
      <p class="person__name">DANIEL MORROW</p>
      <p class="person__credential">P. ENG.</p>
      <p class="person__title">General Manager</p>
    </div>

    <div class="contact">
      <p><span class="contact__label">O.</span>(555) 014-2370 ext.201</p>
      <p><span class="contact__label">P.</span>(555) 019-4482</p>
      <p>dmorrow@steadywave.example</p>
      <p>www.steadywave.example</p>
    </div>

    <div class="company">
      <p class="company__name">STEADYWAVE INC.</p>
      <p>1200 Harbor Line Rd., Suite 101</p>
      <p>Riverton, Ontario, A1A 1A1, Canada</p>
    </div>
  </section>
</body>
</html>
```